Velmar Ops Business Cards

We need to design some upbeat business cards. We are an Industrial Rope Access Company/Height Safety Company that specialize in Rope Access, Confined Space, Anchor Points, Safety Systems, PPE Inspecions and Rigging.
Company name is Velmar Ops Ltd
Card is for Gareth Lomas the Company Director
His mobile number is 027 418 9072 and email is gareth@velmarops.co.nz. Website address is www.velmarops.co.nz.
We will post some pictures below to ensure you get a good idea of what we do.

```html
<!DOCTYPE html>
<html lang="en">
<head>
<meta charset="utf-8">
<title>Velmar Ops Business Cards</title>
<link href="https://fonts.googleapis.com/css2?family=Arimo:wght@400;700&display=swap" rel="stylesheet">
<style>
  :root {
    --backdrop: #3a3430;
    --card-dark: #111111;
    --card-light: #ffffff;
    --ink-light: #f2f2f2;
    --ink-muted: #cfcfcf;
    --ink-dark: #1c1c1c;
    --rule: #5a5a5a;
  }
  * { margin: 0; padding: 0; box-sizing: border-box; }
  html, body {
    width: 1200px; height: 900px; overflow: hidden;
    background: var(--backdrop);
    font-family: "Arimo", Arial, sans-serif;
  }
  .stage {
    position: relative; width: 1200px; height: 900px;
    display: flex; align-items: center; justify-content: center; gap: 40px;
  }
  .card {
    position: relative; width: 520px; height: 300px;
    box-shadow: 0 10px 30px rgba(0,0,0,0.45);
  }
  .card--front { background: var(--card-dark); color: var(--ink-light); }
  .card--back { background: var(--card-light); color: var(--ink-dark);
    display: flex; align-items: center; justify-content: center; }
  .wordmark { font-weight: 700; letter-spacing: 0.5px; white-space: nowrap; }
  .card--front .wordmark {
    position: absolute; right: 36px; top: 88px; font-size: 38px; color: var(--ink-light);
  }
  .card--back .wordmark { font-size: 52px; }
  .divider {
    position: absolute; left: 250px; right: 14px; top: 142px;
    height: 1px; background: var(--rule);
  }
  .contact { position: absolute; left: 44px; bottom: 26px; }
  .contact__name { font-size: 19px; font-weight: 700; text-transform: uppercase; letter-spacing: 0.3px; }
  .contact__role { font-size: 14px; color: var(--ink-muted); margin: 1px 0 12px 6px; }
  .contact__list { list-style: none; margin-left: 24px; }
  .contact__item {
    display: flex; align-items: center; gap: 6px;
    font-size: 15px; color: var(--ink-muted); line-height: 20px;
  }
  .contact__icon { width: 12px; height: 12px; fill: var(--ink-muted); flex: none; }
</style>
</head>
<body>
<main class="stage">
  <section class="card card--front" aria-label="Business card front">
    <div class="wordmark">Velmar Ops</div>
    <div class="divider"></div>
    <div class="contact">
      <div class="contact__name">Gareth Lomas</div>
      <div class="contact__role">Director</div>
      <ul class="contact__list">
        <li class="contact__item">
          <svg class="contact__icon" viewBox="0 0 12 12" aria-hidden="true"><path d="M1 4c0-2 2-3 5-3s5 1 5 3l-2 1-1-2H4L3 5 1 4zM3 6h6l1 5H2l1-5z"/></svg>
          027 418 9072
        </li>
        <li class="contact__item">
          <svg class="contact__icon" viewBox="0 0 12 12" aria-hidden="true"><path d="M0 2h12v8H0z M1 3l5 4 5-4" stroke="#111" stroke-width="1"/></svg>
          gareth@velmarops.co.nz
        </li>
        <li class="contact__item">
          <svg class="contact__icon" viewBox="0 0 12 12" aria-hidden="true"><circle cx="6" cy="6" r="5.5"/><path d="M0.5 6h11M6 0.5c-3 3-3 8 0 11M6 0.5c3 3 3 8 0 11" stroke="#111" stroke-width="0.8" fill="none"/></svg>
          www.velmarops.co.nz
        </li>
      </ul>
    </div>
  </section>
  <section class="card card--back" aria-label="Business card back">
    <div class="wordmark">Velmar Ops</div>
  </section>
</main>
</body>
</html>
```